Masala Kite food truck catering business card

Need business card for indian restaurant - food truck- catering business
Updates

Updated picture of new logo we need on business card

please see new LOGO in picture brief, need card with NEW LOGO

Industry/Entity Type

Indian Restaurant

Requirements
Must have
• Food truck. Catering

Owner Jaspreet Dhillon
Cell: 305-555-0187
Charleston,SC
www.MasalaKiteCharleston.example
www.facebook.com/MasalaKiteCharleston

```html
<!DOCTYPE html>
<html lang="en">
<head>
<meta charset="utf-8">
<title>Masala Kite – Business Card</title>
<link rel="stylesheet" href="https://fonts.googleapis.com/css2?family=Roboto:wght@400;700&display=swap">
<style>
  :root {
    --page-bg: #e9e7e3;
    --card-dark: #262626;
    --card-dark-2: #1b1b1b;
    --lime: #7cc242;
    --plum: #6e1f4f;
    --white: #ffffff;
  }
  html, body {
    margin: 0;
    width: 1200px;
    height: 918px;
    overflow: hidden;
    background: var(--page-bg);
    font-family: "Roboto", Arial, sans-serif;
  }
  .business-card {
    position: absolute;
    left: 100px;
    top: 173px;
    width: 1000px;
    height: 572px;
    overflow: hidden;
    box-shadow: 0 10px 30px rgba(0,0,0,.25);
  }
  .card-texture {
    position: absolute;
    inset: 0;
    background: radial-gradient(ellipse at 40% 40%, var(--card-dark) 0%, var(--card-dark-2) 100%);
  }
  .stripe-art {
    position: absolute;
    inset: 0;
  }
  .brand {
    position: absolute;
    left: 60px;
    top: 48px;
    display: flex;
    align-items: center;
    gap: 18px;
  }
  .brand-name {
    font-weight: 700;
    font-size: 64px;
    line-height: 1;
    color: var(--lime);
    text-transform: uppercase;
    letter-spacing: 1px;
  }
  .brand-dot {
    width: 54px;
    height: 54px;
    border-radius: 50%;
    background: var(--plum);
  }
  .band-text {
    position: absolute;
    left: 60px;
    color: var(--white);
    font-size: 30px;
    line-height: 50px;
    letter-spacing: 1px;
    text-transform: uppercase;
    white-space: nowrap;
  }
  .services { top: 168px; }
  .owner { top: 248px; }
  .contact {
    position: absolute;
    left: 200px;
    display: flex;
    align-items: center;
    gap: 16px;
    color: var(--white);
    font-size: 28px;
    white-space: nowrap;
  }
  .contact svg { width: 28px; height: 28px; flex: none; }
  .contact-phone { top: 316px; }
  .contact-web { top: 412px; }
  .contact-social { top: 506px; }
  .social-dot {
    width: 24px;
    height: 24px;
    border-radius: 50%;
    background: var(--white);
    flex: none;
  }
</style>
</head>
<body>
  <div class="business-card">
    <div class="card-texture" role="img" aria-label="Dark charcoal quilted diamond pattern background"></div>

    <svg class="stripe-art" viewBox="0 0 1000 572" aria-hidden="true">
      <g fill="var(--lime)">
        <polygon points="0,168 720,168 1000,28 1000,76 720,216 0,216"/>
        <polygon points="0,248 720,248 1000,108 1000,156 720,296 0,296"/>
        <polygon points="0,370 720,370 1000,230 1000,258 720,398 0,398"/>
        <polygon points="0,464 720,464 1000,324 1000,352 720,492 0,492"/>
        <polygon points="0,556 720,556 1000,416 1000,444 720,584 0,584"/>
      </g>
    </svg>

    <div class="brand">
      <span class="brand-name">Masala Kite</span>
      <span class="brand-dot"></span>
    </div>

    <div class="band-text services">Food Truk, Catering</div>
    <div class="band-text owner">Jaspreet Dhillon</div>

    <div class="contact contact-phone">
      <svg viewBox="0 0 24 24" aria-hidden="true">
        <rect x="6" y="2" width="12" height="20" rx="2" fill="none" stroke="#fff" stroke-width="2"/>
        <rect x="9" y="5" width="6" height="6" fill="#fff"/>
        <circle cx="12" cy="17" r="1.5" fill="#fff"/>
      </svg>
      <span>305-555-0187</span>
    </div>

    <div class="contact contact-web">
      <svg viewBox="0 0 24 24" aria-hidden="true">
        <circle cx="12" cy="12" r="10" fill="none" stroke="#fff" stroke-width="2"/>
        <ellipse cx="12" cy="12" rx="4" ry="10" fill="none" stroke="#fff" stroke-width="1.5"/>
        <line x1="2" y1="12" x2="22" y2="12" stroke="#fff" stroke-width="1.5"/>
      </svg>
      <span>www.MasalaKiteCharleston.example</span>
    </div>

    <div class="contact contact-social">
      <span class="social-dot"></span>
      <span>/MasalaKiteCharleston</span>
    </div>
  </div>
</body>
</html>
```